Stationary Design for an engineering start-up.

Company name: Lumaret Grain Inc.

Our advanced materials company utilizes a patented process to spray-coat wood surfaces with metal. Metal is sprayed as a super-heated powder and fully conforms to the surface of the wood allowing for a wide range of applications. Metals used are COPPER and BRONZE.

We need a stationary package that includes Business Card, Letter Head, and Envelope.

- After we will submit a contest for a brochure design, so a winning designer will have advantage to take that project as well.

Target Market(s)

Our target market are building and industrial design professionals.

- Architects
- Designers
- Builders

Industry/Entity Type

Engineering

Requirements
Must have
• - All stationary must include our logo (attached)

Sizes:
Business card: Standard 3.5 by 2 inches. Landscape.

Letterhead: 8.5" x 11"

Envelopes:
One standard commercial size #10 (4 1/8" by 9 1/2")
One catalog size envelope (9" by 12")
Assume envelopes are one-sided (front print only)

- Use bleeds where applicable

- Include all fonts used.

File Format:
AI or PSD
** for letterhead please include MSWord template.
Nice to have
• Design style
- Take design style from our logo and attached images.
- Modern, sharp, minimalistic
- Sans fonts
- Don''t be afraid to use color background for business card.
We''re open to ideas of making the business card somehow representative of the product - metal coated wood.

```html
<!DOCTYPE html>
<html lang="en">
<head>
<meta charset="utf-8">
<title>Lumaret Grain Inc. — Stationery Set</title>
<link href="https://fonts.googleapis.com/css2?family=Cabin:wght@500&family=Arimo:wght@400;700&display=swap" rel="stylesheet">
<style>
  :root {
    --backdrop: #a8b4b0;
    --paper: #fdfcfa;
    --wood-dark: #2c0e05;
    --wood: #4a1a0a;
    --copper: #e8892d;
    --sage: #bdbd9f;
    --ink: #1c1c1c;
    --label: #6b2a12;
    --mark: #d8381e;
    --gold-light: #eee8c4;
    --gold-dark: #c8b466;
  }
  * { margin: 0; padding: 0; box-sizing: border-box; }
  html, body { width: 1200px; height: 960px; overflow: hidden; }
  body {
    background: var(--backdrop);
    position: relative;
    font-family: "Arimo", Arial, sans-serif;
    color: var(--ink);
  }
  .piece {
    position: absolute;
    background: var(--paper);
    box-shadow: 2px 3px 4px rgba(0,0,0,.35);
    overflow: hidden;
  }
  .piece--gold {
    background:
      repeating-linear-gradient(90deg, rgba(255,255,255,.12) 0 2px, rgba(0,0,0,.04) 2px 5px),
      linear-gradient(120deg, var(--gold-light), var(--gold-dark));
  }
  .piece svg.edges { position: absolute; inset: 0; width: 100%; height: 100%; }

  .brand { position: absolute; display: flex; align-items: flex-start; gap: 6px; }
  .brand__square { background: var(--mark); flex: none; }
  .brand__text { display: flex; flex-direction: column; }
  .brand__name {
    font-family: "Cabin", Arial, sans-serif;
    font-weight: 500;
    letter-spacing: .06em;
    line-height: 1;
    color: var(--ink);
  }
  .brand__company { color: #333; margin-top: 3px; padding-left: 10px; }

  /* Letterhead */
  .letterhead { left: 5px; top: 18px; width: 458px; height: 593px; }
  .letterhead .brand { left: 22px; top: 32px; }
  .letterhead .brand__square { width: 28px; height: 28px; margin-top: 2px; }
  .letterhead .brand__name { font-size: 25px; }
  .letterhead .brand__company { font-size: 10px; }
  .letterhead__url { position: absolute; left: 270px; top: 28px; color: #e9ddd0; font-size: 12.5px; }
  .letterhead__rule { position: absolute; left: 33px; top: 519px; width: 387px; border-top: 1px solid #bbb; }
  .letterhead__footer { position: absolute; left: 44px; top: 525px; font-size: 8.5px; color: #333; white-space: nowrap; }
  .label { color: var(--label); }
  .footer-gap { margin-left: 14px; }

  /* Business cards */
  .card { width: 352px; height: 202px; }
  .card--front-white { left: 471px; top: 22px; }
  .card--front-gold { left: 836px; top: 21px; }
  .card--back-white { left: 473px; top: 249px; }
  .card--back-gold { left: 835px; top: 248px; }
  .card .brand { left: 48px; top: 15px; }
  .card .brand__square { width: 38px; height: 38px; margin-top: 2px; }
  .card .brand__name { font-size: 33px; }
  .card .brand__company { font-size: 15px; }
  .card__contact {
    position: absolute; right: 60px; top: 82px;
    font-size: 11px; line-height: 13.5px; text-align: right; color: #222;
  }
  .card__contact b { font-weight: 400; color: #000; margin-right: 6px; }
  .card__back {
    position: absolute; inset: 0;
    display: flex; flex-direction: column; align-items: center; padding-top: 42px;
  }
  .card__back .brand__square { width: 40px; height: 40px; }
  .card__back .brand__name { font-size: 33px; margin-top: 10px; letter-spacing: .1em; }
  .card__back-url { font-size: 11.5px; margin-top: 4px; }

  /* Envelopes */
  .envelope-10 { left: 18px; top: 645px; width: 614px; height: 267px; }
  .envelope-10 .brand { left: 52px; top: 12px; }
  .envelope-10 .brand__square { width: 24px; height: 24px; margin-top: 2px; }
  .envelope-10 .brand__name { font-size: 21px; }
  .envelope-10 .brand__company { font-size: 9.5px; }
  .envelope-10 .envelope__rule { left: 148px; top: 244px; width: 438px; }
  .envelope-10 .envelope__footer { left: 158px; top: 248px; }

  .envelope-catalog { left: 643px; top: 534px; width: 542px; height: 380px; }
  .envelope-catalog .brand { left: 55px; top: 22px; }
  .envelope-catalog .brand__square { width: 28px; height: 28px; margin-top: 2px; }
  .envelope-catalog .brand__name { font-size: 23px; }
  .envelope-catalog .brand__company { font-size: 10.5px; }
  .envelope-catalog .envelope__rule { left: 162px; top: 358px; width: 362px; }
  .envelope-catalog .envelope__footer { left: 169px; top: 363px; }

  .envelope__rule { position: absolute; border-top: 1px solid #ccc; }
  .envelope__footer { position: absolute; font-size: 6.8px; color: #333; white-space: nowrap; }
  .envelope__footer .label { font-weight: 700; }
  .envelope__footer .footer-gap { margin-left: 10px; }
</style>
</head>
<body>

<svg width="0" height="0" style="position:absolute" aria-hidden="true">
  <defs>
    <linearGradient id="wood" x1="0" y1="0" x2="1" y2="0.3">
      <stop offset="0" stop-color="#3a1207"/>
      <stop offset=".35" stop-color="#5a2210"/>
      <stop offset=".6" stop-color="#2e0d05"/>
      <stop offset="1" stop-color="#4c1a0b"/>
    </linearGradient>
  </defs>
</svg>

<!-- Letterhead -->
<section class="piece letterhead" aria-label="Letterhead">
  <svg class="edges" viewBox="0 0 458 593" preserveAspectRatio="none" aria-hidden="true">
    <path d="M0,50 C30,44 80,26 135,26 C200,26 250,72 330,72 C380,72 420,58 458,44" fill="none" stroke="var(--sage)" stroke-width="6"/>
    <path d="M0,46 C30,40 80,21 135,20 C200,19 250,67 330,67 C380,67 420,53 458,40" fill="none" stroke="var(--copper)" stroke-width="4"/>
    <path d="M0,0 H458 V37 C420,48 380,64 330,62 C250,58 200,10 135,15 C80,19 30,36 0,42 Z" fill="url(#wood)"/>
    <path d="M0,555 C40,572 80,582 115,580 C200,575 270,530 340,530 C390,530 430,546 458,556" fill="none" stroke="var(--sage)" stroke-width="6"/>
    <path d="M0,559 C40,576 80,586 115,584 C200,579 270,535 340,535 C390,535 430,551 458,561" fill="none" stroke="var(--copper)" stroke-width="4"/>
    <path d="M0,563 C40,580 80,590 115,588 C200,583 270,540 340,540 C390,540 430,555 458,565 V593 H0 Z" fill="url(#wood)"/>
  </svg>
  <div class="brand">
    <span class="brand__square"></span>
    <div class="brand__text">
      <span class="brand__name">LUMARET</span>
      <span class="brand__company">Lumaret Grain Inc.</span>
    </div>
  </div>
  <p class="letterhead__url">www.lumaretgrain.com</p>
  <div class="letterhead__rule"></div>
  <p class="letterhead__footer">12 Avenue St., Sometown, Province, 1A2 3B4<span class="footer-gap label">Tel</span> - 123.456.7890<span class="footer-gap label">Fax</span> - 123.456.7890</p>
</section>

<!-- Business card fronts -->
<section class="piece card card--front-white" aria-label="Business card front, white">
  <svg class="edges" viewBox="0 0 352 202" preserveAspectRatio="none" aria-hidden="true">
    <path d="M36,0 C20,40 16,80 23,110 C28,150 36,180 39,202" fill="none" stroke="var(--sage)" stroke-width="4"/>
    <path d="M33,0 C17,40 13,80 20,110 C25,150 33,180 36,202" fill="none" stroke="var(--copper)" stroke-width="3"/>
    <path d="M0,0 H30 C14,40 10,80 17,110 C22,150 30,180 33,202 H0 Z" fill="url(#wood)"/>
    <path d="M324,0 C337,30 327,80 312,120 C305,150 315,185 327,202" fill="none" stroke="var(--copper)" stroke-width="3"/>
    <path d="M352,0 H327 C340,30 330,80 315,120 C308,150 318,185 330,202 H352 Z" fill="url(#wood)"/>
  </svg>
  <div class="brand">
    <span class="brand__square"></span>
    <div class="brand__text">
      <span class="brand__name">LUMARET</span>
      <span class="brand__company">Lumaret Grain Inc.</span>
    </div>
  </div>
  <p class="card__contact">
    www.lumaretgrain.com<br>
    <b>Address</b>12 Avenue St.<br>Sometown<br>Province<br>1A2 3B4<br>
    <b>Tel</b>123.456.7890<br><b>Fax</b>123.456.7890
  </p>
</section>

<section class="piece piece--gold card card--front-gold" aria-label="Business card front, metallic">
  <svg class="edges" viewBox="0 0 352 202" preserveAspectRatio="none" aria-hidden="true">
    <path d="M36,0 C20,40 16,80 23,110 C28,150 36,180 39,202" fill="none" stroke="var(--sage)" stroke-width="4"/>
    <path d="M33,0 C17,40 13,80 20,110 C25,150 33,180 36,202" fill="none" stroke="var(--copper)" stroke-width="3"/>
    <path d="M0,0 H30 C14,40 10,80 17,110 C22,150 30,180 33,202 H0 Z" fill="url(#wood)"/>
    <path d="M324,0 C337,30 327,80 312,120 C305,150 315,185 327,202" fill="none" stroke="var(--copper)" stroke-width="3"/>
    <path d="M352,0 H327 C340,30 330,80 315,120 C308,150 318,185 330,202 H352 Z" fill="url(#wood)"/>
  </svg>
  <div class="brand">
    <span class="brand__square"></span>
    <div class="brand__text">
      <span class="brand__name">LUMARET</span>
      <span class="brand__company">Lumaret Grain Inc.</span>
    </div>
  </div>
  <p class="card__contact">
    www.lumaretgrain.com<br>
    <b>Address</b>12 Avenue St.<br>Sometown<br>Province<br>1A2 3B4<br>
    <b>Tel</b>123.456.7890<br><b>Fax</b>123.456.7890
  </p>
</section>

<!-- Business card backs -->
<section class="piece card card--back-white" aria-label="Business card back, white">
  <div class="card__back">
    <span class="brand__square"></span>
    <span class="brand__name">LUMARET</span>
    <span class="card__back-url">www.lumaretgrain.com</span>
  </div>
</section>

<section class="piece piece--gold card card--back-gold" aria-label="Business card back, metallic">
  <div class="card__back">
    <span class="brand__square"></span>
    <span class="brand__name">LUMARET</span>
    <span class="card__back-url">www.lumaretgrain.com</span>
  </div>
</section>

<!-- #10 envelope -->
<section class="piece envelope-10" aria-label="Number 10 envelope">
  <svg class="edges" viewBox="0 0 614 267" preserveAspectRatio="none" aria-hidden="true">
    <path d="M41,0 C58,30 61,70 46,110 C31,150 26,200 36,230 C42,250 48,260 53,267" fill="none" stroke="var(--sage)" stroke-width="4"/>
    <path d="M38,0 C55,30 58,70 43,110 C28,150 23,200 33,230 C39,250 45,260 50,267" fill="none" stroke="var(--copper)" stroke-width="3"/>
    <path d="M0,0 H35 C52,30 55,70 40,110 C25,150 20,200 30,230 C36,250 42,260 47,267 H0 Z" fill="url(#wood)"/>
  </svg>
  <div class="brand">
    <span class="brand__square"></span>
    <div class="brand__text">
      <span class="brand__name">LUMARET</span>
      <span class="brand__company">Lumaret Grain Inc.</span>
    </div>
  </div>
  <div class="envelope__rule"></div>
  <p class="envelope__footer"><span class="label">Address</span> - 12 Avenue St., Sometown, Province, 1A2 3B4<span class="footer-gap label">Tel</span> - 123.456.7890<span class="footer-gap label">Fax</span> - 123.456.7890<span class="footer-gap">www.lumaretgrain.com</span></p>
</section>

<!-- Catalog envelope -->
<section class="piece envelope-catalog" aria-label="Catalog envelope">
  <svg class="edges" viewBox="0 0 542 380" preserveAspectRatio="none" aria-hidden="true">
    <path d="M34,0 C57,40 67,100 52,160 C37,220 29,290 37,330 C43,355 49,370 52,380" fill="none" stroke="var(--sage)" stroke-width="5"/>
    <path d="M30,0 C53,40 63,100 48,160 C33,220 25,290 33,330 C39,355 45,370 48,380" fill="none" stroke="var(--copper)" stroke-width="3"/>
    <path d="M0,0 H27 C50,40 60,100 45,160 C30,220 22,290 30,330 C36,355 42,370 45,380 H0 Z" fill="url(#wood)"/>
  </svg>
  <div class="brand">
    <span class="brand__square"></span>
    <div class="brand__text">
      <span class="brand__name">LUMARET</span>
      <span class="brand__company">Lumaret Grain Inc.</span>
    </div>
  </div>
  <div class="envelope__rule"></div>
  <p class="envelope__footer"><span class="label">Address</span> - 12 Avenue St., Sometown, Province 1A2 3B4<span class="footer-gap label">Tel/Fax</span> - 123.456.7890<span class="footer-gap">www.lumaretgrain.com</span></p>
</section>

</body>
</html>
```